Vollo Activewear business card design

I need a business card designed for my activewear business. I would like to use the colours pink, purple white and blue. please see attached logo. please include (name) Rosalind Thwaite (phone) 0417285630 (email) rozzivollo@mailbrook.net (ABN) 51837264019 . please include - Free shipping on all orders over $100

Target Market(s)

female

Contact Information for Business Card

Colors

Designer to choose colors to be used in the design.

Requirements
Must have
• I need a business card designed for my activewear business. I would like to use the colours pink, purple white and blue. please see attached logo. please include (name) Rosalind Thwaite (phone) 0417285630 (email) rozzivollo@mailbrook.net (ABN) 51837264019 . please include - Free shipping on all orders over $100

```html
<!DOCTYPE html>
<html lang="en">
<head>
<meta charset="utf-8">
<title>Vollo Activewear – Business Card</title>
<link href="https://fonts.googleapis.com/css2?family=Noto+Sans:wght@400;600&family=Marcellus&display=swap" rel="stylesheet">
<style>
  :root {
    --backdrop: #2a2a2c;
    --card-dark: #333336;
    --card-light: #ffffff;
    --purple: #9c1fac;
    --mauve: #b4689c;
    --blue: #3f6fd8;
    --steel: #8a8a90;
    --steel-dark: #4a4a4f;
  }
  * { margin: 0; padding: 0; box-sizing: border-box; }
  html, body { width: 1200px; height: 900px; overflow: hidden; }
  body {
    background: var(--backdrop);
    font-family: "Noto Sans", Arial, sans-serif;
    position: relative;
  }
  .card {
    position: absolute;
    left: 290px;
    width: 620px;
    height: 354px;
    overflow: hidden;
  }

  /* Front */
  .card-front {
    top: 60px;
    background: linear-gradient(135deg, #38383b 0%, var(--card-dark) 55%, #2e2e31 100%);
  }
  .front-brand {
    position: absolute;
    left: 38px;
    top: 34px;
    display: flex;
    align-items: center;
    gap: 16px;
  }
  .front-dot {
    width: 40px;
    height: 40px;
    border-radius: 50%;
    background: var(--steel-dark);
  }
  .front-wordmark {
    font-size: 60px;
    font-weight: 600;
    line-height: 1;
    letter-spacing: 3px;
    color: var(--steel);
  }
  .front-frame {
    position: absolute;
    right: 30px;
    bottom: 30px;
    width: 300px;
    height: 180px;
    border-right: 2px solid var(--steel-dark);
    border-bottom: 2px solid var(--steel-dark);
  }
  .front-band {
    position: absolute;
    left: 0;
    right: 0;
    bottom: 0;
    height: 6px;
    background: linear-gradient(90deg, var(--purple), var(--blue));
  }

  /* Back */
  .card-back {
    top: 486px;
    background: var(--card-light);
    border-left: 6px solid var(--purple);
    border-bottom: 6px solid var(--purple);
  }
  .brand {
    position: absolute;
    left: 50px;
    top: 146px;
    display: flex;
    align-items: center;
    gap: 12px;
  }
  .brand-dot {
    width: 30px;
    height: 30px;
    border-radius: 50%;
    background: var(--mauve);
  }
  .brand-name {
    font-size: 38px;
    font-weight: 600;
    line-height: 1;
    letter-spacing: 1px;
    color: var(--purple);
  }
  .brand-rule {
    position: absolute;
    left: 92px;
    top: 196px;
    width: 150px;
    height: 3px;
    background: var(--blue);
  }
  .divider {
    position: absolute;
    left: 300px;
    top: 124px;
    width: 2px;
    height: 104px;
    background: var(--purple);
  }
  .contact {
    position: absolute;
    left: 318px;
    top: 120px;
    color: var(--purple);
    font-size: 17px;
    line-height: 24px;
  }
  .contact-name {
    font-family: "Marcellus", Georgia, serif;
    font-size: 21px;
    letter-spacing: 1.5px;
    color: var(--mauve);
    margin-bottom: 4px;
  }
  .contact-abn { color: var(--purple); }
  .contact-row { display: flex; align-items: center; gap: 8px; }
  .contact-row svg { width: 14px; height: 14px; flex: none; }
  .icon-fill { fill: var(--blue); }
  .icon-line { fill: none; stroke: var(--blue); stroke-width: 2.4; }
  .shipping-note {
    position: absolute;
    left: 0;
    right: 0;
    bottom: 34px;
    text-align: center;
    font-size: 18px;
    color: var(--purple);
  }
</style>
</head>
<body>
  <section class="card card-front">
    <div class="front-brand">
      <span class="front-dot"></span>
      <span class="front-wordmark">VOLLO</span>
    </div>
    <div class="front-frame"></div>
    <div class="front-band"></div>
  </section>

  <section class="card card-back">
    <div class="brand">
      <span class="brand-dot"></span>
      <span class="brand-name">VOLLO</span>
    </div>
    <div class="brand-rule"></div>
    <div class="divider"></div>
    <div class="contact">
      <div class="contact-name">ROSALIND THWAITE</div>
      <div class="contact-abn">ABN 51837264019</div>
      <div class="contact-row">
        <svg viewBox="0 0 24 24"><path class="icon-fill" d="M6.6 10.8a15.1 15.1 0 0 0 6.6 6.6l2.2-2.2a1 1 0 0 1 1-.25 11.4 11.4 0 0 0 3.6.57 1 1 0 0 1 1 1V20a1 1 0 0 1-1 1A17 17 0 0 1 3 4a1 1 0 0 1 1-1h3.5a1 1 0 0 1 1 1c0 1.25.2 2.45.57 3.57a1 1 0 0 1-.25 1z"/></svg>
        <span>0417285630</span>
      </div>
      <div class="contact-row">
        <svg viewBox="0 0 24 24"><path class="icon-line" d="M2 5h20v14H2z M2 5l10 8 10-8"/></svg>
        <span>rozzivollo@mailbrook.net</span>
      </div>
    </div>
    <p class="shipping-note">Free shipping on all orders over $100</p>
  </section>
</body>
</html>
```